Corrow Family Farm fresh honey jar label

I need a label for jars of honey harvested at our farm. These are for gifts and personal use. We are looking to incorporate our farm brand into the label. We would like the design to take the existing brand and add some element like bees, honey, flowers, or hives to indicate the contents. We want the design to feel homemade and authentic without feeling cheap or hoaky

Requirements
Must have
• The label must be made to fit a 1" x2" rectangular label. The label must include the attached family brand. The label must include the text "Corrow Family Farms" "Pinebrook, USA" "Farm Fresh Honey". The label will be printed on off-white paper
Nice to have
• It would be nice to have illustrations of bees or flowers around the logo or hives or honeycombs. The label should have a vintage feel
Should not have
• The label should not feel overly cartoonish or hoaky

```html
<!DOCTYPE html>
<html lang="en">
<head>
<meta charset="utf-8">
<title>Corrow Family Farms – Farm Fresh Honey Label</title>
<link rel="stylesheet" href="https://fonts.googleapis.com/css2?family=Cinzel:wght@400;600&display=swap">
<style>
  :root {
    --paper: #fbfaf6;
    --canvas-bg: #ffffff;
    --bark: #7d6a4c;
    --bark-soft: #a8997f;
    --honey: #c98f2c;
    --sketch: #e9e4d8;
    --sketch-deep: #cfc4ad;
  }
  * { box-sizing: border-box; margin: 0; padding: 0; }
  html, body {
    width: 1200px;
    height: 848px;
    overflow: hidden;
    background: var(--canvas-bg);
  }
  .canvas {
    position: relative;
    width: 1200px;
    height: 848px;
  }
  .label {
    position: absolute;
    left: 420px;
    top: 64px;
    width: 360px;
    height: 720px;
    background: var(--paper);
    border: 14px solid var(--bark);
    font-family: "Cinzel", "Trajan Pro", serif;
    color: var(--bark);
    text-align: center;
  }
  .label__inner-rule {
    position: absolute;
    inset: 8px;
    border: 1.5px solid var(--bark-soft);
  }
  .label__title {
    position: absolute;
    left: 0;
    top: 18px;
    width: 100%;
    height: 150px;
  }
  .label__title text {
    font-family: "Cinzel", serif;
    fill: var(--bark);
  }
  .label__artwork {
    position: absolute;
    left: 22px;
    top: 160px;
    width: 288px;
    height: 260px;
    background: radial-gradient(ellipse at 50% 75%, var(--sketch-deep) 0%, var(--sketch) 45%, var(--paper) 100%);
  }
  .brand-mark {
    position: absolute;
    left: 0;
    top: 190px;
    width: 100%;
    font-size: 44px;
    font-weight: 600;
    letter-spacing: 2px;
    color: var(--bark);
  }
  .label__tagline {
    position: absolute;
    left: 0;
    top: 448px;
    width: 100%;
    font-size: 31px;
    color: var(--honey);
    letter-spacing: 0.5px;
  }
  .label__product {
    position: absolute;
    left: 0;
    top: 478px;
    width: 100%;
    font-size: 70px;
    line-height: 1.1;
    color: var(--honey);
    letter-spacing: 2px;
  }
  .label__divider {
    position: absolute;
    left: 40px;
    top: 572px;
    width: 252px;
    height: 24px;
  }
  .label__place {
    position: absolute;
    left: 0;
    top: 612px;
    width: 100%;
    font-size: 27px;
    color: var(--bark);
  }
</style>
</head>
<body>
<main class="canvas">
  <section class="label" aria-label="Corrow Family Farms honey jar label">
    <div class="label__inner-rule"></div>

    <svg class="label__title" viewBox="0 0 332 150" aria-label="Corrow Family Farms">
      <defs>
        <path id="title-arc" d="M 30 92 Q 166 10 302 92"/>
      </defs>
      <text font-size="30" letter-spacing="1">
        <textPath href="#title-arc" startOffset="50%" text-anchor="middle">CORROW FAMILY,</textPath>
      </text>
      <text x="166" y="130" font-size="31" text-anchor="middle">FARMS</text>
    </svg>

    <div class="label__artwork" role="img" aria-label="Fine line botanical sketch of wildflowers and leaves surrounding an engraved straw beehive skep"></div>

    <div class="brand-mark">Corrow</div>

    <div class="label__tagline">FARM FRESH</div>
    <div class="label__product">HONEY</div>

    <svg class="label__divider" viewBox="0 0 252 24" aria-hidden="true">
      <line x1="24" y1="12" x2="108" y2="12" stroke="var(--honey)" stroke-width="1.5"/>
      <line x1="144" y1="12" x2="228" y2="12" stroke="var(--honey)" stroke-width="1.5"/>
      <rect x="114" y="2" width="24" height="20" fill="var(--bark-soft)" role="img" aria-label="Small engraved honeybee"/>
    </svg>

    <div class="label__place">PINEBROOK, USA</div>
  </section>
</main>
</body>
</html>
```